Migration Lawyers

Company: Dunstan & Co Lawyers & Migration Agents

Name: Graham Dunstan BEc, LLB
Address: Level 18, 72 Hollis Street
Sydney, NSW, Australia 2000

Ph: +61 2 9384 5207
M: 0428316540
E: graham@permitpath-example.org.au
W: www.permitpath-example.org.au

Target Market(s)

Migration Clients

Industry/Entity Type

It Company

Font styles to use
Script

Requirements
Must have
• Logo
Should not have
• Please scale the format to the printing size attached

```html
<!DOCTYPE html>
<html lang="en">
<head>
<meta charset="utf-8">
<title>Dunstan &amp; Co – Business Card</title>
<link rel="stylesheet" href="https://fonts.googleapis.com/css2?family=Open+Sans:wght@400;600;700&display=swap">
<style>
  :root {
    --backdrop: #e7e3de;
    --card: #ffffff;
    --ink: #1c1c1c;
    --ink-soft: #333333;
    --rule: #2a2a2a;
    --shadow: rgba(0, 0, 0, 0.18);
  }
  * { box-sizing: border-box; margin: 0; padding: 0; }
  html, body {
    width: 1200px;
    height: 768px;
    overflow: hidden;
    background: var(--backdrop);
    font-family: "Open Sans", Arial, sans-serif;
    color: var(--ink);
  }
  .stage { position: relative; width: 1200px; height: 768px; }
  .card {
    position: absolute;
    width: 597px;
    height: 340px;
    background: var(--card);
    box-shadow: 0 6px 18px var(--shadow);
  }
  .card--front { left: 102px; top: 30px; }
  .card--back { left: 504px; top: 400px; }

  /* Front */
  .brand { position: absolute; left: 30px; top: 50px; display: flex; align-items: center; gap: 14px; }
  .brand__mark {
    width: 96px; height: 96px;
    border: 2px solid var(--rule);
    border-radius: 50%;
    flex: none;
  }
  .brand__name { font-weight: 700; color: var(--ink); line-height: 1.15; }
  .brand__title { display: block; font-size: 30px; letter-spacing: -0.3px; }
  .brand__sub { display: block; font-size: 13px; }

  .person { position: absolute; right: 24px; top: 172px; text-align: right; }
  .person__name { font-size: 18px; font-weight: 600; }
  .person__creds { font-size: 12.5px; color: var(--ink-soft); margin-top: 2px; }

  .address {
    position: absolute; left: 24px; top: 288px;
    font-size: 13.5px; line-height: 20px; color: var(--ink-soft);
    font-style: normal;
  }
  .contacts {
    position: absolute; right: 24px; top: 274px;
    list-style: none; text-align: right;
    font-size: 13.5px; line-height: 23px; color: var(--ink-soft);
  }
  .contacts li { display: flex; justify-content: flex-end; align-items: center; gap: 6px; }
  .contacts .gap { margin-left: 12px; }
  .icon { width: 12px; height: 12px; flex: none; }

  /* Back */
  .back-brand {
    position: absolute; left: 78px; top: 84px;
    width: 176px; height: 172px;
    border: 2px solid var(--rule);
    border-radius: 50%;
    display: flex; align-items: center; justify-content: center;
  }
  .back-brand__name { font-size: 22px; font-weight: 700; color: var(--ink); }
  .back-url {
    position: absolute; left: 316px; top: 156px;
    font-size: 19px; color: var(--ink-soft);
  }
</style>
</head>
<body>
<main class="stage">

  <section class="card card--front" aria-label="Business card front">
    <div class="brand">
      <span class="brand__mark" aria-hidden="true"></span>
      <p class="brand__name">
        <span class="brand__title">Dunstan &amp; Co</span>
        <span class="brand__sub">Lawyers &amp; Migration Agents</span>
      </p>
    </div>

    <div class="person">
      <p class="person__name">Graham Dunstan</p>
      <p class="person__creds">BEc, LLB</p>
    </div>

    <address class="address">
      Level 18, 72 Hollis Street,<br>
      Australia, Sydney, NSW, 2000
    </address>

    <ul class="contacts">
      <li>
        <svg class="icon" viewBox="0 0 12 12" aria-hidden="true"><path d="M2.5 1 L4.5 1 L5.2 3.6 L4 4.6 Q5 7 7.4 8 L8.4 6.8 L11 7.5 L11 9.5 Q10.5 11 9 11 Q1 10 1 3 Q1 1.5 2.5 1 Z" fill="none" stroke="#333" stroke-width="1"/></svg>
        <span>+61 2 9384 5207</span>
        <svg class="icon gap" viewBox="0 0 12 12" aria-hidden="true"><path d="M2.5 1 L4.5 1 L5.2 3.6 L4 4.6 Q5 7 7.4 8 L8.4 6.8 L11 7.5 L11 9.5 Q10.5 11 9 11 Q1 10 1 3 Q1 1.5 2.5 1 Z" fill="none" stroke="#333" stroke-width="1"/></svg>
        <span>0428316540</span>
      </li>
      <li>
        <svg class="icon" viewBox="0 0 12 12" aria-hidden="true"><rect x="1" y="3" width="10" height="7" fill="#333"/><path d="M1 3 L6 7 L11 3" fill="none" stroke="#fff" stroke-width="1"/></svg>
        <span>graham@permitpath-example.org.au</span>
      </li>
      <li>
        <svg class="icon" viewBox="0 0 12 12" aria-hidden="true"><circle cx="6" cy="6" r="5" fill="none" stroke="#333" stroke-width="1"/><ellipse cx="6" cy="6" rx="2.2" ry="5" fill="none" stroke="#333" stroke-width="0.8"/><path d="M1 6 H11" stroke="#333" stroke-width="0.8"/></svg>
        <span>www.permitpath-example.org.au</span>
      </li>
    </ul>
  </section>

  <section class="card card--back" aria-label="Business card back">
    <div class="back-brand">
      <span class="back-brand__name">Dunstan &amp; Co</span>
    </div>
    <p class="back-url">www.permitpath-example.org.au</p>
  </section>

</main>
</body>
</html>
```